qTorvanix - A forward thinking technology company in the greater Silicon Valley

A .ppt slide deck for a software consulting company. This slide deck will be used for project kick off meetings, sales proposals, and presentations to large audiences that report progress on a variety of projects. It should catch the eye with appealing creativity. Allow for flexibility in space and display. Project well both virtually and in person under varying light conditions. The finished product should give the impression that we are a custom shop but balance in appeal to larger, more traditional companies.

Review of the designs has been delayed due to holiday travel. Thank you for your submissions. I look forward to getting back to you the week of December 3rd.

Target Market(s)

We are an innovative technology company in the greater Silicon Valley. We design and build custom business analytics tools for large, retail corporations. Our solutions deal primarily in the supply chain space but we are leaning towards commercial construction and telecommunications industries. We are targeting prospective clients interested in machine learning and artificial intelligence. Our customers know quality and will pay for a custom solution that exceeds their expectations.

Industry/Entity Type

Business Software

Font styles to use
Sans Serif

Colors

Designer to choose colors to be used in the design.

Requirements
Must have
• Color, graphics, and photos. Multiple different template pages to appeal for graphs, pictures, text, or timelines.
Should not have
• Anything that resembles a "fidget spinner."

```html
<!DOCTYPE html>
<html lang="en">
<head>
<meta charset="utf-8">
<title>qTorvanix – Presentation Template Overview</title>
<link rel="stylesheet" href="https://fonts.googleapis.com/css2?family=Anton&family=Arimo:wght@400;700&family=Montserrat:wght@300;400;500&family=Tinos:wght@400;700&display=swap">
<style>
:root{
  --teal:#25b9a6;
  --teal-dark:#1e9f98;
  --blue:#2a8fd6;
  --green:#3aa57d;
  --ink:#1d1d1d;
  --grey:#6f6f6f;
  --line:#d7d7d7;
  --white:#ffffff;
  --price-head:#8a8a8a;
  --grad:linear-gradient(135deg,#2ec3a5 0%,#28a9c2 50%,#2a8fd6 100%);
  --grad-v:linear-gradient(180deg,#2ec3a5 0%,#2a8fd6 100%);
}
*{margin:0;padding:0;box-sizing:border-box}
html,body{width:1200px;height:2812px;overflow:hidden;background:var(--white)}
body{font-family:"Arimo",Arial,sans-serif;color:var(--ink)}
.deck{display:grid;grid-template-columns:600px 600px;grid-template-rows:repeat(8,351.5px);width:1200px;height:2812px}
.slide{position:relative;overflow:hidden;background:var(--white);box-shadow:inset 0 0 0 1px var(--line)}
.abs{position:absolute}
.grad{background:var(--grad)}
.grad-v{background:var(--grad-v)}
.headline{font-family:"Anton",Impact,sans-serif;font-weight:400;color:var(--ink);letter-spacing:.2px;white-space:nowrap}
.headline.light{color:var(--white)}
.copy{font-size:10px;line-height:14px;color:var(--ink)}
.copy.center{text-align:center}
.copy.justify{text-align:justify}
.copy.light{color:var(--white)}
.green-title{font-family:"Arimo",Arial,sans-serif;font-weight:700;color:var(--green);letter-spacing:1px}
.white-title{font-family:"Arimo",Arial,sans-serif;font-weight:700;color:var(--white);letter-spacing:1px;text-align:center}
.cap-title{font-size:12px;font-weight:700;letter-spacing:.5px;text-align:center}
.placeholder-photo{background:linear-gradient(135deg,#c9cfd3 0%,#8e979c 55%,#4f5a60 100%)}
/* brand */
.brand{display:flex;align-items:center;gap:14px}
.brand-mark{width:34px;height:34px;background:var(--teal)}
.brand-name{font-family:"Montserrat",Arial,sans-serif;font-weight:400;font-size:46px;color:#4f6470}
.tagline{font-family:"Montserrat",Arial,sans-serif;font-weight:500;font-size:20px;color:#8cbf3f}
/* team */
.member{width:180px;text-align:center}
.member-name{font-size:14px;font-weight:700;color:var(--teal);letter-spacing:.5px}
.avatar{width:100px;height:100px;border-radius:50%;margin:10px auto 0;background:linear-gradient(160deg,#dfe7ee,#b9c8d6)}
.member-role{font-size:12px;margin-top:18px;letter-spacing:.5px}
/* timeline */
.tl-line{height:3px;background:rgba(255,255,255,.85)}
.tl-year{font-size:16px;font-weight:700;color:var(--white);width:80px;text-align:center}
.tl-dot{width:10px;height:10px;border-radius:50%;background:var(--white)}
.tl-text{width:100px;text-align:center;font-size:10px;line-height:13px;color:var(--white)}
.tl-text b{display:block;font-size:10px}
/* pricing */
.plan{width:144px}
.plan-head{height:21px;background:var(--price-head);color:var(--white);font-size:13px;text-align:center;line-height:21px}
.plan-price{height:45px;background:var(--white);text-align:center;line-height:45px;font-size:18px;box-shadow:0 1px 0 var(--line)}
.plan-price small{font-size:10px}
.plan-body{height:156px;background:var(--grad-v);color:var(--white);text-align:center;font-size:15px;line-height:22px;padding-top:30px}
/* table */
.price-table{border-collapse:collapse;font-family:"Tinos",serif;font-size:14px}
.price-table th,.price-table td{height:36px;text-align:center;border-bottom:1px solid var(--line)}
.price-table th{font-weight:700;font-size:13px;border-bottom:none}
.price-table td:first-child{text-align:left;text-decoration:underline;text-decoration-color:#c0392b}
/* contact */
.social{display:flex;flex-direction:column;align-items:center;width:90px}
.social-dot{width:34px;height:34px;border-radius:50%;background:#1f5fa8;border:2px solid var(--white)}
.social-label{font-size:11px;line-height:13px;color:var(--white);text-align:center;margin-top:6px}
.contact-item{width:230px;text-align:center;color:var(--white);font-size:15px}
</style>
</head>
<body>
<main class="deck">

<!-- 1 Title -->
<section class="slide title-slide">
  <div class="abs brand" style="left:46px;top:22px"><span class="brand-mark"></span><span class="brand-name">qTorvanix</span></div>
  <div class="abs tagline" style="left:72px;top:78px">Your Partner for Innovative Software Solutions</div>
  <div class="abs placeholder-photo" style="left:0;top:112px;width:600px;height:240px" role="img" aria-label="Photo of a laptop showing a software dashboard on an office desk"></div>
</section>

<!-- 2 About -->
<section class="slide about-slide">
  <h2 class="abs headline" style="left:0;width:560px;text-align:center;top:8px;font-size:40px;padding-left:40px">About us</h2>
  <p class="abs copy center" style="left:112px;top:82px;width:410px">Lorem ipsum dolor sit amet, consectetur adipiscing elit, sed do eiusmod tempor incididunt ut labore et dolore magna aliqua. Ut enim ad minim veniam, quis nostrud exercitation ullamco laboris nisi ut aliquip ex ea commodo consequat. Excepteur sint occaecat cupidatat non proident, sunt in culpa qui officia deserunt mollit anim id est laborum</p>
  <p class="abs copy center" style="left:112px;top:200px;width:410px">Lorem ipsum dolor sit amet, consectetur adipiscing elit, sed do eiusmod tempor incididunt ut labore et dolore magna aliqua. Ut enim ad minim veniam, quis nostrud exercitation ullamco laboris nisi ut aliquip ex ea commodo consequat. Duis aute irure dolor in reprehenderit in voluptate</p>
  <div class="abs grad-v" style="left:545px;top:0;width:27px;height:352px"></div>
</section>

<!-- 3 Team -->
<section class="slide team-slide">
  <h2 class="abs headline" style="left:0;width:600px;text-align:center;top:22px;font-size:40px">Our team</h2>
  <div class="abs member" style="left:30px;top:94px">
    <div class="member-name">NORA L.</div>
    <div class="avatar" role="img" aria-label="Portrait of the CEO"></div>
    <div class="member-role">CEO</div>
    <p class="copy center" style="margin-top:6px">Lorem ipsum dolor sit amet, consectetur adipiscing elit, sed do eiusmod tempor incididunt ut labore et dolore magna aliqua.</p>
  </div>
  <div class="abs member" style="left:210px;top:94px">
    <div class="member-name">PAUL K.</div>
    <div class="avatar" role="img" aria-label="Portrait of the manager"></div>
    <div class="member-role">MANAGER</div>
    <p class="copy center" style="margin-top:6px">Lorem ipsum dolor sit amet, consectetur adipiscing elit, sed do eiusmod tempor incididunt ut labore et dolore magna aliqua.</p>
  </div>
  <div class="abs member" style="left:397px;top:94px">
    <div class="member-name">IRENE V.</div>
    <div class="avatar" role="img" aria-label="Portrait of the director"></div>
    <div class="member-role">DIRECTOR</div>
    <p class="copy center" style="margin-top:6px">Lorem ipsum dolor sit amet, consectetur adipiscing elit, sed do eiusmod tempor incididunt ut labore et dolore magna aliqua.</p>
  </div>
</section>

<!-- 4 Timeline -->
<section class="slide timeline-slide grad">
  <h2 class="abs headline light" style="left:0;width:600px;text-align:center;top:12px;font-size:34px">Our company in the time</h2>
  <p class="abs copy center light" style="left:50px;top:74px;width:500px">Lorem ipsum dolor sit amet, consectetur adipiscing elit, sed do eiusmod tempor incididunt ut labore et dolore magna aliqua. Ut enim ad minim veniam, quis nostrud exercitation ullamco laboris nisi ut aliquip ex ea commodo consequat</p>
  <div class="abs tl-line" style="left:40px;top:192px;width:480px"></div>
  <div class="abs tl-year" style="left:58px;top:155px">2016</div>
  <div class="abs tl-year" style="left:174px;top:153px">2017</div>
  <div class="abs tl-year" style="left:292px;top:153px">2018</div>
  <div class="abs tl-year" style="left:404px;top:150px">2019</div>
  <div class="abs tl-dot" style="left:93px;top:188px"></div>
  <div class="abs tl-dot" style="left:209px;top:188px"></div>
  <div class="abs tl-dot" style="left:327px;top:188px"></div>
  <div class="abs tl-dot" style="left:439px;top:188px"></div>
  <svg class="abs" style="left:508px;top:162px" width="64" height="64" viewBox="0 0 64 64" aria-hidden="true">
    <circle cx="32" cy="32" r="30" fill="rgba(255,255,255,.35)"/>
    <circle cx="32" cy="32" r="22" fill="var(--teal)" stroke="#fff" stroke-width="2"/>
    <circle cx="32" cy="32" r="9" fill="none" stroke="#fff" stroke-width="4" stroke-dasharray="4 3"/>
    <circle cx="32" cy="32" r="4" fill="#fff"/>
  </svg>
  <div class="abs tl-text" style="left:48px;top:228px"><b>Your Text Here</b>You can simply impress your audience and add a unique zing.</div>
  <div class="abs tl-text" style="left:164px;top:228px"><b>Your Text Here</b>You can simply impress your audience and add a unique zing.</div>
  <div class="abs tl-text" style="left:282px;top:228px"><b>Your Text Here</b>You can simply impress your audience and add a unique zing.</div>
  <div class="abs tl-text" style="left:394px;top:228px"><b>Your Text Here</b>You can simply impress your audience and add a unique zing.</div>
</section>

<!-- 5 Three columns -->
<section class="slide columns-slide">
  <h2 class="abs headline" style="left:0;width:600px;text-align:center;top:14px;font-size:28px">Three colums text</h2>
  <p class="abs copy justify" style="left:34px;top:76px;width:172px;font-size:9px;line-height:13px">Lorem ipsum dolor sit amet, consectetur adipiscing elit, sed do eiusmod tempor incididunt ut labore et dolore magna aliqua. Ut enim ad minim veniam, quis nostrud exercitation ullamco laboris nisi ut aliquip ex ea commodo consequat.<br><br>Duis aute irure dolor in reprehenderit in voluptate velit esse cillum dolore eu fugiat nulla pariatur. Excepteur sint occaecat cupidatat non proident, sunt</p>
  <p class="abs copy justify" style="left:225px;top:76px;width:170px;font-size:9px;line-height:13px">in culpa qui officia deserunt mollit anim id est laborum<br><br>Lorem ipsum dolor sit amet, consectetur adipiscing elit, sed do eiusmod tempor incididunt ut labore et dolore magna aliqua. Ut enim ad minim veniam, quis nostrud exercitation ullamco laboris nisi ut.<br><br>Duis aute irure dolor in reprehenderit in voluptate velit esse cillum dolore eu fugiat nulla pariatur. Excepteur sint</p>
  <p class="abs copy justify" style="left:409px;top:76px;width:172px;font-size:9px;line-height:13px">occaecat cupidatat non proident, sunt in culpa qui officia deserunt mollit anim id est laborum<br><br>Lorem ipsum dolor sit amet, consectetur adipiscing elit, sed do eiusmod tempor incididunt ut labore et dolore magna aliqua. Ut enim ad minim veniam, quis nostrud exercitation ullamco laboris nisi ut aliquip ex.</p>
</section>

<!-- 6 Panel left + two features -->
<section class="slide feature-slide">
  <div class="abs grad-v" style="left:0;top:0;width:188px;height:352px"></div>
  <h3 class="abs white-title" style="left:10px;width:168px;top:40px;font-size:17px;line-height:20px">Write here a title</h3>
  <p class="abs copy center light" style="left:14px;top:92px;width:160px">Lorem ipsum dolor sit amet, consectetur adipiscing elit, sed do eiusmod tempor incididunt ut labore et dolore magna aliqua. Ut enim ad minim veniam, quis nostrud exercitation ullamco laboris nisi ut aliquip ex ea commodo consequat.</p>
  <svg class="abs" style="left:274px;top:46px" width="32" height="30" viewBox="0 0 32 30" aria-hidden="true"><rect x="2" y="2" width="28" height="20" fill="none" stroke="var(--green)" stroke-width="2"/><rect x="8" y="12" width="3" height="7" fill="var(--green)"/><rect x="14" y="8" width="3" height="11" fill="var(--green)"/><rect x="20" y="10" width="3" height="9" fill="var(--green)"/><path d="M16 22v5M10 28h12" stroke="var(--green)" stroke-width="2"/></svg>
  <svg class="abs" style="left:468px;top:44px" width="34" height="32" viewBox="0 0 34 32" aria-hidden="true"><rect x="3" y="22" width="5" height="8" fill="var(--green)"/><rect x="11" y="17" width="5" height="13" fill="var(--green)"/><rect x="19" y="20" width="5" height="10" fill="var(--green)"/><rect x="27" y="12" width="5" height="18" fill="var(--green)"/><path d="M3 16l9-8 6 5 12-11" stroke="var(--green)" stroke-width="2.5" fill="none"/><path d="M24 2h7v7" stroke="var(--green)" stroke-width="2.5" fill="none"/></svg>
  <div class="abs cap-title" style="left:219px;width:140px;top:102px">LOREM IPSUM</div>
  <div class="abs cap-title" style="left:415px;width:140px;top:102px">LOREM IPSUM</div>
  <p class="abs copy justify" style="left:222px;top:122px;width:136px">Lorem ipsum dolor sit amet, consectetur adipiscing elit, sed do eiusmod tempor incididunt ut labore et dolore magna aliqua. Ut enim ad minim veniam, quis nostrud exercitation ullamco laboris nisi ut aliquip ex ea commodo consequat.</p>
  <p class="abs copy justify" style="left:418px;top:122px;width:136px">Lorem ipsum dolor sit amet, consectetur adipiscing elit, sed do eiusmod tempor incididunt ut labore et dolore magna aliqua. Ut enim ad minim veniam, quis nostrud exercitation ullamco laboris nisi ut aliquip ex ea commodo consequat.</p>
</section>

<!-- 7 Photo grid -->
<section class="slide photo-grid-slide">
  <h3 class="abs green-title" style="left:20px;width:262px;text-align:center;top:16px;font-size:20px">Write here a title</h3>
  <p class="abs copy center" style="left:34px;top:52px;width:250px">Lorem ipsum dolor sit amet, consectetur adipiscing elit, sed do eiusmod tempor incididunt ut labore et dolore magna aliqua. Ut enim ad minim veniam, quis nostrud exercitation ullamco laboris nisi ut aliquip ex ea commodo consequat.</p>
  <div class="abs placeholder-photo" style="left:300px;top:0;width:300px;height:175px;background:linear-gradient(135deg,#5b6670,#1f2a33 60%,#4a6a86)" role="img" aria-label="Photo of hands typing code on a laptop"></div>
  <div class="abs placeholder-photo" style="left:0;top:175px;width:300px;height:177px;background:linear-gradient(135deg,#2c2f33,#51565c 60%,#9aa1a7)" role="img" aria-label="Photo of a cursor clicking a settings button on a screen"></div>
  <h3 class="abs green-title" style="left:300px;width:300px;text-align:center;top:196px;font-size:20px">Write here a title</h3>
  <p class="abs copy center" style="left:320px;top:234px;width:264px">Lorem ipsum dolor sit amet, consectetur adipiscing elit, sed do eiusmod tempor incididunt ut labore et dolore magna aliqua. Ut enim ad minim veniam, quis nostrud exercitation ullamco laboris nisi ut aliquip ex ea commodo consequat.</p>
</section>

<!-- 8 Two features + panel right -->
<section class="slide feature-slide">
  <svg class="abs" style="left:98px;top:46px" width="32" height="30" viewBox="0 0 32 30" aria-hidden="true"><rect x="2" y="2" width="28" height="20" fill="none" stroke="var(--green)" stroke-width="2"/><rect x="8" y="12" width="3" height="7" fill="var(--green)"/><rect x="14" y="8" width="3" height="11" fill="var(--green)"/><rect x="20" y="10" width="3" height="9" fill="var(--green)"/><path d="M16 22v5M10 28h12" stroke="var(--green)" stroke-width="2"/></svg>
  <svg class="abs" style="left:292px;top:44px" width="34" height="32" viewBox="0 0 34 32" aria-hidden="true"><rect x="3" y="22" width="5" height="8" fill="var(--green)"/><rect x="11" y="17" width="5" height="13" fill="var(--green)"/><rect x="19" y="20" width="5" height="10" fill="var(--green)"/><rect x="27" y="12" width="5" height="18" fill="var(--green)"/><path d="M3 16l9-8 6 5 12-11" stroke="var(--green)" stroke-width="2.5" fill="none"/><path d="M24 2h7v7" stroke="var(--green)" stroke-width="2.5" fill="none"/></svg>
  <div class="abs cap-title" style="left:44px;width:140px;top:100px">LOREM IPSUM</div>
  <div class="abs cap-title" style="left:240px;width:140px;top:100px">LOREM IPSUM</div>
  <p class="abs copy justify" style="left:46px;top:120px;width:136px">Lorem ipsum dolor sit amet, consectetur adipiscing elit, sed do eiusmod tempor incididunt ut labore et dolore magna aliqua. Ut enim ad minim veniam, quis nostrud exercitation ullamco laboris nisi ut aliquip ex ea commodo consequat.</p>
  <p class="abs copy justify" style="left:242px;top:120px;width:136px">Lorem ipsum dolor sit amet, consectetur adipiscing elit, sed do eiusmod tempor incididunt ut labore et dolore magna aliqua. Ut enim ad minim veniam, quis nostrud exercitation ullamco laboris nisi ut aliquip ex ea commodo consequat.</p>
  <div class="abs grad-v" style="left:426px;top:0;width:174px;height:352px"></div>
  <h3 class="abs white-title" style="left:434px;width:158px;top:38px;font-size:17px;line-height:20px">Write here a title</h3>
  <p class="abs copy center light" style="left:436px;top:92px;width:154px">Lorem ipsum dolor sit amet, consectetur adipiscing elit, sed do eiusmod tempor incididunt ut labore et dolore magna aliqua. Ut enim ad minim veniam, quis nostrud exercitation ullamco laboris nisi ut aliquip ex ea commodo consequat.</p>
</section>

<!-- 9 Title + three items -->
<section class="slide list-slide grad">
  <div class="abs" style="left:184px;top:0;width:2px;height:352px;background:rgba(255,255,255,.8)"></div>
  <h2 class="abs headline light" style="left:20px;width:320px;text-align:center;top:134px;font-size:40px;line-height:50px;white-space:normal">WRITE HERE<br>A TITLE</h2>
  <svg class="abs" style="left:425px;top:4px" width="22" height="20" viewBox="0 0 22 20" aria-hidden="true"><path d="M2 18h18" stroke="#fff" stroke-width="2"/><rect x="4" y="10" width="3" height="7" fill="#fff"/><rect x="10" y="5" width="3" height="12" fill="#fff"/><rect x="16" y="2" width="3" height="15" fill="#fff"/></svg>
  <div class="abs white-title" style="left:360px;width:200px;top:40px;font-size:17px;text-align:left;font-weight:400;letter-spacing:0">Write Here a Title</div>
  <p class="abs copy light" style="left:360px;top:64px;width:200px;font-size:9px;line-height:12px;opacity:.85">Lorem ipsum dolor sit amet, consectetur adipiscing elit, sed do eiusmod tempor incididunt ut.</p>
  <svg class="abs" style="left:425px;top:120px" width="22" height="20" viewBox="0 0 22 20" aria-hidden="true"><rect x="2" y="2" width="18" height="12" fill="none" stroke="#fff" stroke-width="2"/><path d="M11 14v4M6 18h10" stroke="#fff" stroke-width="2"/></svg>
  <div class="abs white-title" style="left:360px;width:200px;top:156px;font-size:17px;text-align:left;font-weight:400;letter-spacing:0">Write Here a Title</div>
  <p class="abs copy light" style="left:360px;top:180px;width:200px;font-size:9px;line-height:12px;opacity:.85">Lorem ipsum dolor sit amet, consectetur adipiscing elit, sed do eiusmod tempor incididunt ut.</p>
  <svg class="abs" style="left:425px;top:236px" width="22" height="20" viewBox="0 0 22 20" aria-hidden="true"><path d="M1 2h4l3 10h10l2-7H7" stroke="#fff" stroke-width="2" fill="none"/><circle cx="9" cy="16" r="2" fill="#fff"/><circle cx="17" cy="16" r="2" fill="#fff"/></svg>
  <div class="abs white-title" style="left:360px;width:200px;top:272px;font-size:17px;text-align:left;font-weight:400;letter-spacing:0">Write Here a Title</div>
  <p class="abs copy light" style="left:360px;top:296px;width:200px;font-size:9px;line-height:12px;opacity:.85">Lorem ipsum dolor sit amet, consectetur adipiscing elit, sed do eiusmod tempor incididunt ut.</p>
</section>

<!-- 10 Services -->
<section class="slide services-slide">
  <div class="abs" style="left:105px;top:0;width:2px;height:100px;background:var(--teal)"></div>
  <div class="abs" style="left:105px;top:232px;width:2px;height:120px;background:var(--teal)"></div>
  <h2 class="abs headline" style="left:26px;width:200px;text-align:center;top:128px;font-size:34px;line-height:40px;white-space:normal">OUR<br>SERVICES</h2>
  <div class="abs green-title" style="left:224px;width:170px;text-align:center;top:22px;font-size:13px;letter-spacing:0">Write Here a Title</div>
  <p class="abs copy center" style="left:224px;top:42px;width:170px">An per utinam intellegat reprehendunt, vel eu aperiri delenit corrumpit. Cu duo virtute eligendi.</p>
  <div class="abs green-title" style="left:412px;width:170px;text-align:center;top:22px;font-size:13px;letter-spacing:0">Write Here a Title</div>
  <p class="abs copy center" style="left:412px;top:42px;width:170px">Vel eu nulla alterum referrentur. An mel sensibus molestiae, eos sint elitr dissentias et. Graeci utroque volutpat.</p>
  <div class="abs green-title" style="left:224px;width:170px;text-align:center;top:138px;font-size:13px;letter-spacing:0">Write Here a Title</div>
  <p class="abs copy center" style="left:224px;top:158px;width:170px">Ut vitae pericula mea. Nulla appareat inciderint ut eum, sea eu semper fuisset.</p>
  <div class="abs green-title" style="left:412px;width:170px;text-align:center;top:138px;font-size:13px;letter-spacing:0">Write Here a Title</div>
  <p class="abs copy center" style="left:412px;top:158px;width:170px">Eros recusabo ut sit. Possim facilisis adolescens ad duo, at veniam tamquam.</p>
  <div class="abs green-title" style="left:224px;width:170px;text-align:center;top:236px;font-size:13px;letter-spacing:0">Write Here a Title</div>
  <p class="abs copy center" style="left:224px;top:256px;width:170px">Mei ad inani accusamus moderatius. Ne pri voluptua postulant, eu eos antiopam erroribus instructior.</p>
  <div class="abs green-title" style="left:412px;width:170px;text-align:center;top:236px;font-size:13px;letter-spacing:0">Write Here a Title</div>
  <p class="abs copy center" style="left:412px;top:256px;width:170px">No vel vidit ridens gubergren. Ea quo etiam malorum assentior, sit cu legendos platonem cotidieque.</p>
</section>

<!-- 11 Pricing cards -->
<section class="slide pricing-slide">
  <h2 class="abs headline" style="left:0;width:600px;text-align:center;top:8px;font-size:36px">Sales proposals</h2>
  <p class="abs copy center" style="left:40px;top:64px;width:520px">Homero docendi deque vix eu. Per laoreet legendos ad, tempor gubergren reformidans vix ad.</p>
  <div class="abs plan" style="left:56px;top:107px"><div class="plan-head">Midi</div><div class="plan-price">$20.99<small>/month</small></div><div class="plan-body">10 accounts<br>2,000 items<br>25 Gb storage</div></div>
  <div class="abs plan" style="left:226px;top:107px"><div class="plan-head">Mini</div><div class="plan-price">$9.99<small>/month</small></div><div class="plan-body" style="padding-top:50px">5 accounts<br>1,000 items<br>10 Gb storage</div></div>
  <div class="abs plan" style="left:401px;top:107px"><div class="plan-head">Maxi</div><div class="plan-price">$50.99<small>/month</small></div><div class="plan-body">20 accounts<br>Unlimited<br>100 Gb storage</div></div>
</section>

<!-- 12 Illustration card -->
<section class="slide showcase-slide grad">
  <div class="abs" style="left:60px;top:24px;width:500px;height:314px;background:var(--white);transform:skewX(-7deg)"></div>
  <h3 class="abs" style="left:114px;top:80px;font-family:'Tinos',serif;font-weight:400;font-size:28px;letter-spacing:1px">LOREM IPSUM</h3>
  <p class="abs copy" style="left:114px;top:122px;width:200px">Lorem ipsum dolor sit amet, consectetur adipiscing elit, sed do eiusmod tempor incididunt ut labore et dolore magna aliqua. Ut enim ad minim veniam, quis nostrud exercitation ullamco laboris nisi ut aliquip ex ea commodo consequat.</p>
  <div class="abs" style="left:330px;top:60px;width:226px;height:246px;border-radius:40% 40% 12px 12px;background:linear-gradient(160deg,#ece6f5,#c9c3e0 60%,#dfe9f2)" role="img" aria-label="Illustration of three people working together at a table with laptops"></div>
</section>

<!-- 13 Quote -->
<section class="slide quote-slide">
  <div class="abs grad" style="left:56px;top:42px;width:516px;height:260px"></div>
  <div class="abs" style="left:72px;top:68px;width:488px;height:182px;background:var(--white)"></div>
  <svg class="abs" style="left:28px;top:28px" width="84" height="56" viewBox="0 0 84 56" aria-hidden="true"><path d="M4 4h30v26L16 52V30H4z M46 4h30v26L58 52V30H46z" fill="var(--teal-dark)"/></svg>
  <blockquote class="abs" style="left:96px;top:88px;width:440px;text-align:center;font-family:'Tinos',serif;font-weight:700;font-size:25px;line-height:34px">Be who you are and say what you feel, because those who mind don't matter, and those who matter don't mind</blockquote>
  <div class="abs" style="left:56px;width:516px;top:266px;text-align:center;font-family:'Tinos',serif;font-weight:700;font-size:12px;color:var(--white)">Edwin R. Calloway</div>
</section>

<!-- 14 Pricing table -->
<section class="slide table-slide">
  <h2 class="abs headline" style="left:0;width:600px;text-align:center;top:10px;font-size:36px">Sales proposals</h2>
  <p class="abs copy center" style="left:60px;top:70px;width:480px;font-size:11px;line-height:15px">Homero docendi deque vix eu. Per laoreet legendos ad, tempor gubergren reformidans vix ad.</p>
  <div class="abs" style="left:173px;top:152px;width:133px;height:166px;border:2px solid var(--teal)"></div>
  <table class="abs price-table" style="left:40px;top:128px;width:540px">
    <colgroup><col style="width:130px"><col style="width:133px"><col style="width:133px"><col style="width:144px"></colgroup>
    <tr><th></th><th>Basic</th><th>Pro</th><th>Ultimate</th></tr>
    <tr><td>Fee</td><td><b>20$</b></td><td>50$</td><td>100$</td></tr>
    <tr><td>GB</td><td><b>100</b></td><td>1000</td><td>Unlimited</td></tr>
    <tr><td>Icons</td><td><b>100</b></td><td>300</td><td>Unlimited</td></tr>
    <tr><td>Elements</td><td><b>250</b></td><td>500</td><td>Unlimited</td></tr>
  </table>
</section>

<!-- 15 Contact -->
<section class="slide contact-slide grad">
  <div class="abs" style="left:285px;top:0;width:2px;height:110px;background:rgba(255,255,255,.8)"></div>
  <div class="abs" style="left:285px;top:214px;width:2px;height:138px;background:rgba(255,255,255,.8)"></div>
  <h2 class="abs headline light" style="left:181px;width:210px;text-align:center;top:124px;font-size:38px;line-height:44px;white-space:normal">CONTACT<br>US</h2>
  <div class="abs social" style="left:74px;top:36px"><span class="social-dot"></span><span class="social-label">Write your<br>text</span></div>
  <div class="abs social" style="left:74px;top:140px"><span class="social-dot" style="background:#1c7bb8"></span><span class="social-label">Write your<br>text</span></div>
  <div class="abs social" style="left:74px;top:244px"><span class="social-dot" style="background:#39a6e8"></span><span class="social-label">Write your<br>text</span></div>
  <svg class="abs" style="left:428px;top:28px" width="32" height="32" viewBox="0 0 32 32" aria-hidden="true"><path d="M8 3l6 6-3 4c2 4 4 6 8 8l4-3 6 6-4 5C14 28 4 18 3 8z" fill="none" stroke="#fff" stroke-width="2"/></svg>
  <div class="abs contact-item" style="left:329px;top:80px">+314 555 010 482</div>
  <svg class="abs" style="left:428px;top:128px" width="34" height="34" viewBox="0 0 34 34" aria-hidden="true"><g fill="none" stroke="#fff" stroke-width="2"><circle cx="17" cy="17" r="14"/><ellipse cx="17" cy="17" rx="6" ry="14"/><path d="M3 17h28M6 9h22M6 25h22"/></g></svg>
  <div class="abs contact-item" style="left:329px;top:172px">https://qtorvanixlabs.com</div>
  <svg class="abs" style="left:428px;top:244px" width="36" height="26" viewBox="0 0 36 26" aria-hidden="true"><g fill="none" stroke="#fff" stroke-width="2"><rect x="2" y="2" width="32" height="22"/><path d="M2 2l16 13L34 2M2 24l12-11M34 24L22 13"/></g></svg>
  <div class="abs contact-item" style="left:329px;top:284px">E-mail</div>
</section>

<!-- 16 Thank you -->
<section class="slide thanks-slide" style="background:linear-gradient(90deg,#a79bd0 0%,#3fc1b2 45%,#2a8fd6 100%)">
  <div class="abs" style="left:160px;top:34px;width:284px;height:284px;border-radius:50%;background:var(--white);box-shadow:0 0 0 6px rgba(255,255,255,.45)"></div>
  <div class="abs" style="left:0;width:604px;top:132px;display:flex;justify-content:center"><span style="width:22px;height:22px;background:var(--teal)"></span></div>
  <div class="abs" style="left:0;width:604px;text-align:center;top:166px;font-family:'Montserrat',Arial,sans-serif;font-weight:400;font-size:32px;color:var(--teal)">THANK YOU</div>
</section>

</main>
</body>
</html>
```